Very Simple/Minimal Business Card Design Project

The company operates in the industrial maritime infrastructure sector in Brazil. You can find more information on our website www.navelquor.com.br WE NEED TO LOOK POWERFUL AND SERIOUS
I have attached a copy of the old cards. We would like something more professional / industrial / sexy that also includes the position.

The card can be double sided or not. We would like you to propose as many options.

Thank you
Updates

Many thanks, do let me know if you have any questions. I am under a lot of time pressure to try and have them printed over the next days or so.

Please could you use the following information

for the address: Rua Tapiraçu, 418 - Centro, Rio de Janeiro, 20135-070, Brasil

for the mobile: +55 21 8372 9041
for the landline: +55 21 4067 3859

and position:  Diretor Geral

Thakn you

Target Market(s)

Shipowners, bankers, industrial companies

Industry/Entity Type

Industrial

Requirements
Must have
• POWERFUL
SERIOUS
SOLID
BIG CORPORATION

```html
<!DOCTYPE html>
<html lang="pt-BR">
<head>
<meta charset="utf-8">
<title>Navelquor Business Card</title>
<link rel="stylesheet" href="https://fonts.googleapis.com/css2?family=Titillium+Web:wght@400;600;700&display=swap">
<style>
  :root {
    --bg: #e9eaec;
    --green: #1f9e4a;
    --green-light: #4cc277;
    --navy: #34458a;
    --navy-deep: #222d63;
    --navy-text: #2e3a7c;
    --silver-light: #f4f4f5;
    --silver-mid: #c9cacc;
    --silver-dark: #9d9ea1;
    --ink: #333438;
    --white: #ffffff;
  }
  * { box-sizing: border-box; margin: 0; padding: 0; }
  html, body { width: 1200px; height: 861px; overflow: hidden; }
  body {
    background: var(--bg);
    font-family: "Titillium Web", sans-serif;
    position: relative;
  }
  .card {
    position: absolute;
    top: 287px;
    width: 500px;
    height: 286px;
    overflow: hidden;
    background: linear-gradient(105deg, var(--silver-light) 0%, var(--silver-mid) 55%, var(--silver-dark) 80%, var(--silver-light) 100%);
    box-shadow: 0 10px 28px rgba(0,0,0,0.18);
  }
  .card--front { left: 60px; }
  .card--back { left: 640px; }

  /* plain colour bands */
  .band { position: absolute; left: 0; right: 0; }
  .band--top {
    top: 0; height: 52px;
    background: linear-gradient(90deg, var(--green-light), var(--green));
    border-bottom: 6px solid var(--white);
  }
  .band--bottom {
    bottom: 0;
    background: linear-gradient(90deg, var(--navy), var(--navy-deep));
    border-top: 6px solid var(--white);
  }
  .card--front .band--bottom { height: 84px; }
  .card--back .band--bottom { height: 148px; }
  .corner {
    position: absolute; top: 0; right: 0;
    width: 210px; height: 104px;
    background: var(--green);
    clip-path: polygon(0 0, 100% 0, 100% 100%);
  }

  .brand {
    position: absolute;
    display: flex;
    align-items: center;
    gap: 10px;
  }
  .brand__square { background: var(--green); border-radius: 5px; }
  .brand__name {
    color: var(--navy-text);
    font-weight: 700;
    letter-spacing: 0.5px;
    line-height: 1;
  }
  .card--front .brand { left: 0; right: 0; top: 92px; justify-content: center; }
  .card--front .brand__square { width: 44px; height: 44px; }
  .card--front .brand__name { font-size: 40px; }
  .website {
    position: absolute; left: 0; right: 0; top: 146px;
    text-align: center; color: var(--ink);
    font-weight: 700; font-size: 16px;
  }

  .card--back .brand { left: 38px; top: 30px; }
  .card--back .brand__square { width: 40px; height: 40px; }
  .card--back .brand__name { font-size: 34px; }

  .contact { position: absolute; left: 36px; right: 20px; top: 166px; color: var(--white); }
  .contact__name { font-size: 21px; font-weight: 700; letter-spacing: 0.4px; }
  .contact__role { font-size: 11px; font-weight: 400; letter-spacing: 0.4px; }
  .contact__line { font-size: 11.5px; margin-top: 8px; white-space: nowrap; }
  .contact__label { font-weight: 700; }
  .contact__grid {
    display: grid; grid-template-columns: 220px 1fr; margin-top: 14px;
    font-size: 11.5px; line-height: 1.45; white-space: nowrap;
  }
</style>
</head>
<body>

<section class="card card--front">
  <div class="band band--top"></div>
  <div class="band band--bottom"></div>
  <div class="brand">
    <span class="brand__square"></span>
    <span class="brand__name">NAVELQUOR</span>
  </div>
  <p class="website">www.navelquor.com.br</p>
</section>

<section class="card card--back">
  <div class="corner"></div>
  <div class="band band--bottom"></div>
  <div class="brand">
    <span class="brand__square"></span>
    <span class="brand__name">NAVELQUOR</span>
  </div>
  <div class="contact">
    <p><span class="contact__name">RAFAEL MOREIRA</span> <span class="contact__role">| DIRETOR GERAL</span></p>
    <p class="contact__line"><span class="contact__label">Office</span> Rua Tapiraçu, 418 - Centro, Rio de Janeiro, 20135-070, Brasil</p>
    <div class="contact__grid">
      <p><span class="contact__label">Telephone</span> +55 21 4067 3859<br><span class="contact__label">Mobile</span> +55 21 8372 9041</p>
      <p><span class="contact__label">E-mail</span> rafael@navelquor.com.br<br><span class="contact__label">Website</span> www.navelquor.com.br</p>
    </div>
  </div>
</section>

</body>
</html>
```